Webdesign für Marke KLARWERK plus
Zielgruppe
K+W Zielwertkraft besteht seit 1995 und war zunächst jahrzehntelang als klassische Werbeagentur mit den Schwerpunkten Print, VKF und TV tätig. In den vergangenen Jahren hat sich unsere unternehmerische Ausrichtung jedoch zunehmend auf die Bereiche Expansion, Akquisition und Consulting verlagert –hier sind wir schwerpunktmäßig für zwei große deutsche Unternehmen als etablierter Dienstleister tätig.
Aktuell forcieren wir nun unsere Marke KLARWERK plus. Schwerpunkt von KLARWERK plus ist es, das Thema „Hygiene-Auftritt“ künftig zum Bestandteil einer zukunftsorientierten Unternehmensführung bzw. eines erfolgreichen Marketing-Mix zu machen. Zunächst starten wir mit zwei hochwertigen Varianten von wohl einzigartigen Desinfektionsgeräten, die Qualität, Design und eine hohe Marken- Individualisierbarkeit vereinen. Zielgruppe ist der Gesamtbereich B-to-B.
Aufgabenstellung
Aktuell existiert eine erste Broschüre, die aber nicht zwingend das 'Maß der Dinge' sein muss - wir sind da ganz offen! Diese Broschüre fügen wir als pdf bei. Sie ist sehr kurzfristig auf dei beine gestellt worden, vielleicht ist sie auch 'zu un-emotional' und insofern zu wenig zum Kauf anregend. Dann schlagen SIE doch eine andere Art von Website vor!

```html
<!DOCTYPE html>
<html lang="de">
<head>
<meta charset="utf-8">
<title>KLARWERK plus – Unsere Mission</title>
<link href="https://fonts.googleapis.com/css2?family=Montserrat:wght@500;600;700&family=Poppins:wght@300;400;500&display=swap" rel="stylesheet">
<style>
  :root {
    --gold: #dcc257;
    --ink: #1e1e1e;
    --text: #555555;
    --muted: #9a9a9a;
    --panel: #f4f4f4;
    --dark: #232323;
    --dark-2: #333333;
    --white: #ffffff;
  }
  * { box-sizing: border-box; margin: 0; padding: 0; }
  html, body { width: 1200px; height: 2349px; overflow: hidden; background: var(--white); }
  body { position: relative; font-family: "Poppins", sans-serif; color: var(--text); }
  .abs { position: absolute; }

  .brand { font-family: "Montserrat", sans-serif; font-weight: 700; color: var(--ink); letter-spacing: 0.5px; }
  .brand--header { left: 55px; top: 15px; font-size: 13px; }
  .brand--footer { left: 55px; top: 2236px; font-size: 15px; }

  .main-nav a { position: absolute; top: 18px; font-size: 11px; color: var(--muted); text-decoration: none; }
  .main-nav a.is-active { color: var(--ink); font-weight: 500; }
  .main-nav .active-mark { position: absolute; left: 797px; top: 30px; color: var(--gold); font-size: 10px; }

  .plus { position: absolute; }
  .plus::before, .plus::after { content: ""; position: absolute; background: var(--gold); }
  .plus--page { left: 50px; top: 100px; width: 40px; height: 40px; }
  .plus--page::before { left: 0; top: 18px; width: 40px; height: 4px; }
  .plus--page::after { left: 18px; top: 0; width: 4px; height: 40px; }
  .plus--dark { left: 94px; top: 1561px; width: 26px; height: 26px; }
  .plus--dark::before { left: 0; top: 12px; width: 26px; height: 3px; }
  .plus--dark::after { left: 12px; top: 0; width: 3px; height: 26px; }

  .page-title { left: 91px; top: 140px; font-family: "Montserrat", sans-serif; font-weight: 700; font-size: 62px; color: var(--ink); letter-spacing: -0.5px; }

  .icon-panel { position: absolute; width: 335px; height: 203px; background: var(--panel); display: flex; align-items: center; justify-content: center; }
  .icon-panel::after { content: ""; position: absolute; bottom: -2px; width: 130px; height: 2px; background: var(--gold); }
  .icon-panel--left { left: 0; }
  .icon-panel--left::after { left: 0; }
  .icon-panel--right { left: 866px; width: 334px; }
  .icon-panel--right::after { right: 0; }

  .feature-title { position: absolute; font-family: "Montserrat", sans-serif; font-weight: 600; font-size: 25px; color: var(--ink); }
  .rule { position: absolute; width: 50px; height: 1px; background: var(--gold); }
  .feature-text { position: absolute; font-size: 11.5px; line-height: 17px; color: var(--text); }
  .feature-text p + p { margin-top: 17px; }

  .service-divider { left: 1005px; top: 935px; width: 1px; height: 114px; background: #d8d8d8; }
  .service-label { left: 1047px; top: 975px; font-family: "Montserrat", sans-serif; font-size: 9.5px; letter-spacing: 2px; color: #666; font-weight: 500; }
  .service-number { left: 1047px; top: 992px; font-family: "Montserrat", sans-serif; font-size: 13px; font-weight: 600; color: var(--ink); }

  .dark-block { left: 0; top: 1491px; width: 770px; height: 627px; background: var(--dark); }
  .dark-side { left: 844px; top: 1491px; width: 356px; height: 431px; background: var(--dark); }
  .product-visual { left: 967px; top: 1441px; width: 127px; height: 415px; border-radius: 4px;
    background: linear-gradient(100deg, #cfcfcf 0%, #ffffff 45%, #e4e4e4 75%, #bdbdbd 100%); }
  .dark-caption { left: 814px; top: 1922px; width: 386px; height: 128px; background: var(--dark-2); padding: 20px 18px 0 17px; font-size: 9px; line-height: 14px; color: #c9c9c9; }
  .dark-caption p + p { margin-top: 14px; }

  .dark-title { left: 119px; top: 1585px; font-family: "Montserrat", sans-serif; font-weight: 600; font-size: 27px; line-height: 31px; color: var(--white); }
  .dark-subtitle { left: 119px; top: 1703px; font-family: "Montserrat", sans-serif; font-weight: 600; font-size: 16px; color: var(--white); }
  .dark-text { left: 185px; top: 1734px; width: 510px; font-size: 11.5px; line-height: 17px; color: #dcdcdc; }
  .dark-text p + p { margin-top: 17px; }
  .cta { left: 185px; top: 2038px; font-family: "Montserrat", sans-serif; font-size: 10px; font-weight: 600; letter-spacing: 2px; color: var(--gold); text-decoration: none; }
  .cta-circle { left: 436px; top: 2033px; width: 23px; height: 23px; border: 1px solid #cfcfcf; border-radius: 50%; display: flex; align-items: center; justify-content: center; }

  .footer-line { left: 0; top: 2205px; width: 1200px; height: 1px; background: #e2e2e2; }
  .copyright { left: 50px; top: 2309px; font-size: 11px; color: var(--ink); }
  .footer-col { position: absolute; top: 2232px; text-align: right; }
  .footer-col h4 { font-family: "Montserrat", sans-serif; font-weight: 500; font-size: 11px; letter-spacing: 2px; color: var(--ink); margin-bottom: 3px; }
  .footer-col a { display: block; font-size: 9.5px; line-height: 19.3px; color: #444; text-decoration: none; }
</style>
</head>
<body>

<header>
  <div class="abs brand brand--header">KLARWERK plus</div>
  <nav class="main-nav">
    <a style="left:680px">Home</a>
    <a class="is-active" style="left:762px">Unsere Mission</a>
    <span class="active-mark">+</span>
    <a style="left:891px">Produkte</a>
    <a style="left:990px">Der Mehrwert</a>
    <a style="left:1110px">Kontakt</a>
  </nav>
</header>

<main>
  <span class="plus plus--page"></span>
  <h1 class="abs page-title">Unsere Mission</h1>

  <!-- Starke Marke -->
  <div class="icon-panel icon-panel--left" style="top:286px">
    <svg width="64" height="40" viewBox="0 0 64 40" fill="none" stroke="#1e1e1e" stroke-width="4">
      <polyline points="2,37 20,20 32,30 58,5"/>
      <polyline points="40,4 60,4 60,24"/>
    </svg>
  </div>
  <h2 class="feature-title" style="left:398px;top:298px">Starke Marke</h2>
  <span class="rule" style="left:398px;top:353px"></span>
  <div class="feature-text" style="left:465px;top:344px;width:565px">
    <p>“KLARWERK plus”: Da weiß jeder sofort, worum es geht. Dieser einprägsame Markenname stellt somit die optimale Basis für eine starke Marke dar, die wir sukzessive entwickeln werden: Sowohl hinsichtlich des inhaltlichen Portfolios an Geräten und Dienstleistungen, als auch im Sinne der gesamten Markenbildung.</p>
    <p>Positiver Nebeneffekt unseres Markennamens: KLARWERK plus ist hinsichtlich seiner Schreibweise international adaptierbar…</p>
  </div>

  <!-- Qualität und Design -->
  <h2 class="feature-title" style="left:91px;top:599px">Qualität und Design</h2>
  <span class="rule" style="left:91px;top:653px"></span>
  <div class="feature-text" style="left:159px;top:645px;width:585px">
    <p>Ein Markenname impliziert auch Verantwortung im Sinne hoher Qualität und daher werden die von KLARWERK plus angebotenen Geräte ausschließlich in Deutschland bzw. in Europa gefertigt.</p>
    <p>“Design-orientiert und trotzdem sehr<br>robust” lautet eine weitere Qualitätsmaxime, denn alle unsere Geräte sind  für den harten Dauergebrauch im öffentlichen Raum konzipiert.</p>
  </div>
  <div class="icon-panel icon-panel--right" style="top:577px">
    <svg width="68" height="68" viewBox="0 0 68 68" fill="none" stroke="#1e1e1e" stroke-width="3.5">
      <circle cx="34" cy="34" r="31"/>
      <path d="M22 10 C28 16 36 12 40 16 C44 20 50 22 50 30 C50 38 42 42 38 52 C36 58 32 62 30 62 C28 54 26 46 20 42 C14 38 10 32 14 24 C16 18 18 14 22 10 Z"/>
    </svg>
  </div>

  <!-- Full-Service -->
  <div class="icon-panel icon-panel--left" style="top:869px">
    <svg width="68" height="66" viewBox="0 0 68 66" fill="none" stroke="#1e1e1e" stroke-width="4">
      <path d="M34 2 C51 2 65 15 65 32 L65 64 L34 64 C17 64 3 50 3 33 C3 16 17 2 34 2 Z"/>
      <circle cx="22" cy="34" r="1.8" fill="#1e1e1e"/>
      <circle cx="34" cy="34" r="1.8" fill="#1e1e1e"/>
      <circle cx="46" cy="34" r="1.8" fill="#1e1e1e"/>
    </svg>
  </div>
  <h2 class="feature-title" style="left:398px;top:889px">Full-Service</h2>
  <span class="rule" style="left:398px;top:945px"></span>
  <div class="feature-text" style="left:465px;top:936px;width:505px">
    <p>Es versteht sich von selbst, dass  eine unserer Missionen auch ein zuverlässiger Full-Service in allen Bereichen ist: Angefangen mit zuverlässiger Lieferfähigkeit der Hygiene-Stationen, über den schnellen Versand von Verbrauchsmaterialien  bis hin zu telefonischem Support über unsere Servicenummer.</p>
    <p>Ab Anfang 2021 planen wir für die Premium-Station das Angebot eines Mietkaufs.</p>
  </div>
  <span class="abs service-divider"></span>
  <div class="abs service-label">SERVICENUMMER</div>
  <div class="abs service-number">0800 415 2763</div>

  <!-- Individualisierbarkeit -->
  <h2 class="feature-title" style="left:91px;top:1181px">Individualisierbarkeit</h2>
  <span class="rule" style="left:91px;top:1236px"></span>
  <div class="feature-text" style="left:159px;top:1227px;width:560px">
    <p>Die Notwendigkeit von Hygiene- Maßnahmen wird auf unabsehbare Zeit bleiben und insofern ist genau jetzt der richtige Zeitpunkt, um den Gesamtbereich der Hygiene zum Teil der Markenstrategie eines Unternehmens zu machen.</p>
    <p>KLARWERK plus bietet hierzu ein umfassendes “Baukastensystem der Individualisierbarkeit”. Viele interessante Details hierzu erfahren Sie auf den folgenden Seiten.</p>
  </div>
  <div class="icon-panel icon-panel--right" style="top:1160px">
    <svg width="70" height="70" viewBox="0 0 70 70" fill="none" stroke="#1e1e1e" stroke-width="3.5">
      <rect x="2" y="2" width="66" height="66" rx="3"/>
      <line x1="2" y1="56" x2="68" y2="56"/>
      <polyline points="2,44 22,26 48,48"/>
      <circle cx="50" cy="20" r="6"/>
    </svg>
  </div>

  <!-- Weiterentwicklung -->
  <section>
    <div class="abs dark-block"></div>
    <div class="abs dark-side"></div>
    <div class="abs product-visual" role="img" aria-label="Freistehende weiße Desinfektionsstation mit Bildschirm und Spenderfächern"></div>
    <div class="abs dark-caption">
      <p>So, wie der Homo Sapiens genetisch gesehen nach-gewiesenermaßen noch gar nicht fertig ist, verhält es sich mit zahlreichen technischen Entwicklungen rund um  KLARWERK plus:</p>
      <p>Lassen Sie sich in den nächsten Jahren überraschen, was hier noch alles kommen wird!</p>
    </div>

    <span class="plus plus--dark"></span>
    <h2 class="abs dark-title">Weiterentwicklung steckt<br>in unseren Genen</h2>
    <h3 class="abs dark-subtitle">Neuerfindungen und Portfolioerweiterung</h3>
    <span class="rule" style="left:119px;top:1745px"></span>
    <div class="abs dark-text">
      <p>Ein “KLARWERK plus-Gedanke” wird auch noch lange nach Corona in den Köpfen und somit in den Verhaltensweisen eines jeden Menschen weltweit verankert bleiben. Grund genug, dass KLARWERK plus als Marke sowohl dem Bereich Produktneuentwicklung als auch der Erweiterung des Produktport-folios hohe Bedeutung beimessen wird.</p>
      <p>Einige Weiterentwicklungen wie z.B. Premium-Säulen mit integrierten, für jeglichen Content nutzbaren Informations-Screens sind bereits ebenso in Arbeit wie die Integration von Fiebermess-Screens.</p>
      <p>Auch im Bereich “Raumlüftung” wird im Jahr 2021 eine Portfolio-Erweiter-ung stattfinden.</p>
      <p>Last but not least: Wir stehen bereits mit einem der renommierten Wissen- schaftler von denen man täglich in der Presse liest in Kontakt, um eine langfristig besonders fachkompetente Ausrichtung der Marke KLARWERK plus zu erreichen.</p>
    </div>
    <a class="abs cta">ENTDECKEN SIE UNSERE PRODUKTE</a>
    <span class="abs cta-circle">
      <svg width="10" height="8" viewBox="0 0 10 8" fill="none" stroke="#ffffff" stroke-width="1.2"><line x1="1" y1="4" x2="9" y2="4"/><polyline points="6,1 9,4 6,7"/></svg>
    </span>
  </section>
</main>

<footer>
  <span class="abs footer-line"></span>
  <div class="abs brand brand--footer">KLARWERK plus</div>
  <div class="abs copyright">© 2020</div>
  <div class="footer-col" style="right:297px">
    <h4>NAVIGATION</h4>
    <a>Home</a><a>Unsere Mission</a><a>Produkte</a><a>Der Mehrwert</a>
  </div>
  <div class="footer-col" style="right:185px">
    <h4>KONTAKT</h4>
    <a>Kontaktformular</a>
  </div>
  <div class="footer-col" style="right:50px">
    <h4>RECHTLICHES</h4>
    <a>Datenschutz</a><a>AGB</a><a>Impressum</a>
  </div>
</footer>

</body>
</html>
```